pet minder needs a flyer design

I need a flyer design for my pet minding/ dog walking business.
My business is called 'Muddy paws happy tail crew', i would like the business
name included in on the flyer (i dont mind how big or small it is)
i was hoping for a design that was warm and friendly and obviously
incorporates animals :)
I have attached the information i would like included on the flyer below

Target Market(s)

all ages.

Industry/Entity Type

Pet Care

Font styles to use
Serif

Colors
ec1f27

Requirements
Must have
• information about the services i provide
• incorporates animals
Nice to have
• colour red

```html
<!DOCTYPE html>
<html lang="en">
<head>
<meta charset="utf-8">
<title>Muddy paws happy tail crew – Petsitter Flyer</title>
<link href="https://fonts.googleapis.com/css2?family=Arimo:wght@700&family=Merriweather:wght@700&display=swap" rel="stylesheet">
<style>
  :root {
    --frame: #4a2b16;
    --red: #e21f24;
    --yellow: #fff200;
    --white: #ffffff;
    --ink: #111111;
    --paw: #f7941d;
    --dog: #f39a5b;
  }
  * { margin: 0; padding: 0; box-sizing: border-box; }
  html, body { width: 867px; height: 1200px; overflow: hidden; background: var(--frame); }
  .flyer {
    position: relative;
    width: 867px; height: 1200px;
    border: 17px solid var(--frame);
    background: var(--red);
    font-family: 'Arimo', Arial, sans-serif;
    font-weight: 700;
  }
  .headline {
    position: absolute; left: 18px; top: 32px;
    width: 615px; height: 96px;
    background: var(--white);
    border-radius: 0 10px 10px 0;
    color: var(--ink);
    font-size: 48px;
    line-height: 96px;
    padding-left: 26px;
  }
  .header-paws { position: absolute; right: 20px; top: 18px; width: 150px; height: 140px; }
  .intro {
    position: absolute; left: 23px; top: 163px;
    width: 305px; height: 487px;
    background: var(--yellow);
    color: var(--red);
    font-size: 31px;
    line-height: 51px;
    text-align: center;
    padding-top: 36px;
  }
  .photo {
    position: absolute; left: 338px; top: 163px;
    width: 475px; height: 500px;
    border: 5px solid var(--white);
    background: linear-gradient(180deg, #dfe9f2 0%, #c9b48e 32%, #6f9a3c 45%, #4f7f2a 100%);
  }
  .services-tab {
    position: absolute; left: 23px; top: 683px;
    width: 340px; height: 52px;
    background: var(--yellow);
    clip-path: polygon(0 0, 90% 0, 100% 50%, 90% 100%, 0 100%);
    color: var(--red);
    font-size: 32px;
    line-height: 52px;
    padding-left: 22px;
  }
  .services { position: absolute; left: 23px; top: 780px; width: 600px; color: var(--white); font-size: 34px; list-style: none; }
  .service { position: absolute; display: flex; align-items: center; gap: 14px; white-space: nowrap; }
  .service svg { width: 38px; height: 38px; flex: none; }
  .dog-art {
    position: absolute; left: 608px; top: 760px;
    width: 225px; height: 200px;
    background: radial-gradient(ellipse at 55% 55%, var(--dog) 0%, rgba(243,154,91,0.55) 45%, rgba(226,31,36,0) 75%);
  }
  .business-name {
    position: absolute; left: 0; top: 990px;
    width: 833px;
    text-align: center;
    color: var(--yellow);
    font-family: 'Merriweather', Georgia, serif;
    font-size: 26px;
    line-height: 36px;
  }
  .contact {
    position: absolute; left: 0; top: 1038px;
    width: 833px; height: 95px;
    background: var(--yellow);
    color: var(--ink);
    font-size: 44px;
    line-height: 95px;
    padding-left: 26px;
  }
  .contact .name { color: var(--red); }
</style>
</head>
<body>
<svg width="0" height="0" style="position:absolute">
  <defs>
    <symbol id="paw" viewBox="0 0 40 40">
      <ellipse cx="8" cy="16" rx="4.5" ry="6"/>
      <ellipse cx="16" cy="8" rx="4.5" ry="6"/>
      <ellipse cx="25" cy="8" rx="4.5" ry="6"/>
      <ellipse cx="33" cy="16" rx="4.5" ry="6"/>
      <path d="M20 19c-7 0-13 9-13 14 0 4 4 5 7 4 3-1 4-2 6-2s3 1 6 2c3 1 7 0 7-4 0-5-6-14-13-14z"/>
    </symbol>
  </defs>
</svg>
<main class="flyer">
  <h1 class="headline">Do you need a petsitter?</h1>
  <svg class="header-paws" viewBox="0 0 150 140" fill="var(--paw)" aria-hidden="true">
    <use href="#paw" x="0" y="0" width="40" height="40"/>
    <use href="#paw" x="55" y="50" width="50" height="50"/>
    <use href="#paw" x="105" y="15" width="42" height="42"/>
  </svg>

  <p class="intro">I am a fully<br>qualified veterinary<br>nurse who will<br>look after your<br>animals like<br>they were my<br>own own,<br>when you go away!</p>

  <div class="photo" role="img" aria-label="Photo of the pet sitter walking two large dogs on a lawn in front of a building"></div>

  <h2 class="services-tab">Services Provide</h2>

  <ul class="services">
    <li class="service" style="left:0;top:0"><svg fill="var(--paw)"><use href="#paw"/></svg>Pet Minding</li>
    <li class="service" style="left:275px;top:0"><svg fill="var(--paw)"><use href="#paw"/></svg>House Sitting</li>
    <li class="service" style="left:0;top:75px"><svg fill="var(--paw)"><use href="#paw"/></svg>Dog Walking</li>
    <li class="service" style="left:275px;top:75px"><svg fill="var(--paw)"><use href="#paw"/></svg>Medication</li>
    <li class="service" style="left:0;top:145px"><svg fill="var(--paw)"><use href="#paw"/></svg>Collecting Mail/Watering Plants</li>
  </ul>

  <div class="dog-art" role="img" aria-label="Illustration of a sitting dog wearing a collar"></div>

  <p class="business-name">Muddy paws happy tail crew</p>

  <p class="contact">enquire call me: <span class="name">Tessa 0400 000 123</span></p>
</main>
</body>
</html>
```